Healing stone/crystal Shopify store

Hi - I'm creating a new site to sell healing crystals/stones.Name for the shop is LumaraBloomHouse. Site helps people to choose best crystals for them .Shop should have blog aswell.The site should be informative and attractive. Stones we sell Opalite,Green Aventurine,Watermelon Crystal,Rose Quartz Stone,Tiger Eye Stone. Must be Shopify. No content yet, you can fill neccessary fields Lorea Ipsum and if you have some good idea you can put it there
Updates

Designs look the same

Target Market(s)

Woman, English speaking countries.

Industry/Entity Type

Shop

Number of Pages Required

1 page

Colors

Designer to choose colors to be used in the design.

Requirements
Must have
• Blog
Nice to have
• High quality pictures to look site attractive.

```html
<!DOCTYPE html>
<html lang="en">
<head>
<meta charset="utf-8">
<title>Lumara Bloom House – Healing Crystals</title>
<link href="https://fonts.googleapis.com/css2?family=Oswald:wght@400;500;600&family=PT+Sans:ital,wght@0,400;0,700;1,400&display=swap" rel="stylesheet">
<style>
:root{
  --ink:#111111;
  --text:#333333;
  --muted:#8a8a8a;
  --line:#d9d9d9;
  --gold:#c08a2e;
  --card:#f5f5f5;
  --soft:#f7f7f7;
  --white:#ffffff;
  --dark-panel:#2a2a2a;
  --chirper:#1da1f2;
  --searchly:#d9392c;
  --friendbook:#3b5998;
}
*{box-sizing:border-box;margin:0;padding:0}
html,body{width:1200px;height:2317px;overflow:hidden}
body{position:relative;background:var(--white);font-family:"PT Sans",sans-serif;color:var(--text)}
.abs{position:absolute}

/* top bar */
.topbar{left:0;top:0;width:1200px;height:40px;border-bottom:1px solid var(--line);font-size:12px;color:#555}
.topbar .contact{left:199px;top:12px;display:flex;gap:22px;align-items:center}
.topbar .contact span{display:flex;align-items:center;gap:7px}
.topbar .account{right:199px;top:12px;display:flex;gap:8px;align-items:center}

/* header */
.header{left:0;top:40px;width:1200px;height:93px}
.logo{left:199px;top:23px;width:216px;height:47px;border:1.5px solid var(--ink);display:flex;align-items:center;justify-content:center;font-family:"Oswald",sans-serif;font-weight:500;font-size:22px;color:var(--ink);letter-spacing:.2px}
.nav{top:39px;font-size:11.5px;font-weight:700;color:var(--ink);letter-spacing:.3px}
.search{left:880px;top:38px;font-size:12px;color:#777;display:flex;gap:10px;align-items:center}
.header .divider{left:962px;top:28px;width:1px;height:32px;background:var(--line)}
.cart-icon{left:980px;top:38px}

/* hero */
.hero{left:0;top:133px;width:1200px;height:526px}
.hero-panel{top:0;height:526px}
.hero-copy{left:597px;top:0;width:300px;height:526px;text-align:center;color:var(--white)}
.hero-title{position:absolute;top:176px;width:100%;font-family:"Oswald",sans-serif;font-weight:500;font-size:34px;color:var(--gold)}
.hero-sub{position:absolute;top:230px;width:100%;font-size:12.5px;font-weight:700;letter-spacing:.2px}
.hero-btn{position:absolute;left:95px;top:295px;width:111px;height:40px;border:1.5px solid var(--white);display:flex;align-items:center;justify-content:center;font-size:12px;font-weight:700}

/* features */
.feature{top:697px;display:flex;align-items:center;gap:14px}
.feature .ring{width:56px;height:56px;border:1.5px solid #ddd;border-radius:50%;display:flex;align-items:center;justify-content:center}
.feature h4{font-size:11.5px;font-weight:700;color:var(--ink);margin-bottom:2px}
.feature p{font-size:11px;color:#9a9a9a}

/* section headings */
.section-rule{left:0;width:1200px;height:1px;background:var(--line)}
.section-title{left:0;width:1200px;text-align:center;font-family:"Oswald",sans-serif;font-weight:500;font-size:33px;color:var(--gold)}

/* products */
.product{width:184px;text-align:center}
.product .thumb{width:184px;height:198px;background:var(--card);border:1px solid #dedede}
.product h3{margin-top:9px;font-size:11.5px;font-weight:700;color:var(--ink);letter-spacing:.2px}
.product .price{font-size:12px;font-style:italic;color:#555;margin-top:2px}
.product .add{margin:10px auto 0;width:94px;height:32px;background:var(--ink);color:var(--white);font-size:11px;font-weight:700;display:flex;align-items:center;justify-content:center}
.quick-tools{left:156px;top:115px;display:flex;flex-direction:column;gap:5px}
.quick-tools span{width:22px;height:22px;background:var(--ink);display:flex;align-items:center;justify-content:center}

/* blog */
.post{top:1681px;width:387px;height:178px}
.post .day{position:absolute;left:0;top:26px;font-family:"PT Sans",sans-serif;font-size:38px;font-weight:700;color:var(--ink);letter-spacing:1px}
.post .month{position:absolute;left:60px;top:33px;font-size:11.5px;color:var(--ink);line-height:1.55}
.post .headline{position:absolute;left:0;top:78px;width:170px;font-size:11.5px;font-weight:700;color:var(--ink);line-height:1.6}
.post .meta{position:absolute;left:0;top:134px;font-size:10.5px;color:#777;display:flex;align-items:center;gap:10px}
.post .meta i{width:1px;height:16px;background:#ccc;display:block}
.post .photo{position:absolute;left:181px;top:0;width:206px;height:178px}
.blog-arrows{left:976px;top:1663px}

/* newsletter */
.newsletter{left:0;top:1927px;width:1200px;height:390px;background:linear-gradient(180deg,#f7f7f7 0%,#f4f3f1 45%,#e4ddd3 100%)}
.newsletter h2{position:absolute;top:108px;width:100%;text-align:center;font-family:"Oswald",sans-serif;font-weight:400;font-size:17px;color:var(--ink)}
.newsletter .lead{position:absolute;top:133px;width:100%;text-align:center;font-size:12px;color:#555}
.email-field{position:absolute;left:374px;top:171px;width:349px;height:37px;background:#e9e9e9;font-size:11px;color:#666;padding-left:17px;display:flex;align-items:center}
.signup-btn{position:absolute;left:730px;top:171px;width:88px;height:37px;background:var(--ink);color:var(--white);font-size:12px;font-weight:700;display:flex;align-items:center;justify-content:center}
.social-row{position:absolute;left:405px;top:240px;display:flex;align-items:center;gap:10px}
.social-row .label{font-size:12px;font-weight:700;color:var(--ink);margin-right:6px}
.social-btn{height:26px;padding:0 10px;color:var(--white);font-size:11.5px;display:flex;align-items:center;gap:6px}
.social-btn i{width:8px;height:8px;border-radius:50%;background:var(--white);display:block}
.social-btn.chirper{background:var(--chirper);width:77px}
.social-btn.searchly{background:var(--searchly);width:77px}
.social-btn.friendbook{background:var(--friendbook);width:91px}
.footer-rule{position:absolute;left:0;width:1200px;height:1px;background:#bdbdbd}
.footer-links{position:absolute;top:302px;width:100%;display:flex;justify-content:center;gap:26px;font-size:11.5px;font-weight:700;color:var(--ink)}
.copyright{position:absolute;top:350px;width:100%;text-align:center;font-size:11.5px;color:var(--ink)}
</style>
</head>
<body>

<!-- top bar -->
<div class="abs topbar">
  <div class="abs contact">
    <span><svg width="11" height="11" viewBox="0 0 24 24"><path fill="#777" d="M6.6 10.8a15 15 0 0 0 6.6 6.6l2.2-2.2c.3-.3.7-.4 1-.2 1.1.4 2.3.6 3.6.6.6 0 1 .4 1 1V20c0 .6-.4 1-1 1A17 17 0 0 1 3 4c0-.6.4-1 1-1h3.5c.6 0 1 .4 1 1 0 1.3.2 2.5.6 3.6.1.3 0 .7-.2 1z"/></svg>Call Us : +1987650432</span>
    <span><svg width="13" height="10" viewBox="0 0 26 20"><rect x="1" y="1" width="24" height="18" fill="none" stroke="#777" stroke-width="2"/><path d="M1 1l12 10L25 1" fill="none" stroke="#777" stroke-width="2"/></svg>E-mail : info@lumarabloomhouse.com</span>
  </div>
  <div class="abs account">
    <svg width="11" height="11" viewBox="0 0 24 24"><circle cx="12" cy="7" r="5" fill="#777"/><path d="M2 24c0-6 4.5-9 10-9s10 3 10 9z" fill="#777"/></svg>
    <span>Account</span><span>|</span><span>Login</span>
  </div>
</div>

<!-- header -->
<header class="abs header">
  <div class="abs logo">LUMARA BLOOM HOUSE</div>
  <nav>
    <span class="abs nav" style="left:466px">HOME</span>
    <span class="abs nav" style="left:533px">ABOUT US</span>
    <span class="abs nav" style="left:624px">PRODUCT</span>
    <span class="abs nav" style="left:710px">BLOG</span>
    <span class="abs nav" style="left:774px">CONTACT US</span>
  </nav>
  <div class="abs search">Search
    <svg width="11" height="11" viewBox="0 0 24 24"><circle cx="10" cy="10" r="7" fill="none" stroke="#777" stroke-width="3"/><path d="M15 15l7 7" stroke="#777" stroke-width="3"/></svg>
  </div>
  <div class="abs divider"></div>
  <svg class="abs cart-icon" width="17" height="15" viewBox="0 0 26 22"><path d="M1 2h4l3 12h13l3-9H7" fill="none" stroke="#111" stroke-width="2.4"/><circle cx="10" cy="19" r="2" fill="#111"/><circle cx="19" cy="19" r="2" fill="#111"/></svg>
</header>

<!-- hero -->
<section class="abs hero">
  <div class="abs hero-panel" style="left:0;width:298px;background:linear-gradient(135deg,#3a3a44 0%,#7c7c86 45%,#d6d6dc 100%)" role="img" aria-label="Ring of carved clear and smoky quartz angel figurines on a dark surface"></div>
  <div class="abs hero-panel" style="left:298px;width:299px;background:radial-gradient(ellipse at 50% 50%,#2a2f6e 0%,#3b3f7a 18%,#f3f3f3 34%,#f1f1f1 100%)" role="img" aria-label="Blue sodalite angel figurine on a light grey background"></div>
  <div class="abs hero-panel" style="left:597px;width:300px;background:linear-gradient(180deg,#1f1f1f 0%,#3a3a3a 55%,#5a5a5a 100%)" role="img" aria-label="Darkened image of a ring of crystal angel figurines"></div>
  <div class="abs hero-panel" style="left:897px;width:303px;background:radial-gradient(ellipse at 52% 45%,#7a4b22 0%,#9a6634 18%,#ececec 38%,#ececec 100%)" role="img" aria-label="Tiger eye stone elephant figurine on a light grey background"></div>
  <div class="abs hero-copy">
    <div class="hero-title">Lumara Bloom House</div>
    <div class="hero-sub">SHOP LUMARA BLOOM HOUSE TODAY</div>
    <div class="hero-btn">SHOP NOW</div>
  </div>
</section>

<!-- features -->
<div class="abs feature" style="left:199px">
  <div class="ring"><svg width="26" height="18" viewBox="0 0 26 18"><rect x="1" y="2" width="15" height="10" fill="#999"/><path d="M16 5h5l4 4v3h-9z" fill="#999"/><circle cx="6" cy="14" r="2.5" fill="#999"/><circle cx="20" cy="14" r="2.5" fill="#999"/></svg></div>
  <div><h4>FREE SHIPPING</h4><p>Lorem Ipsum is simply</p></div>
</div>
<div class="abs feature" style="left:513px">
  <div class="ring"><svg width="22" height="18" viewBox="0 0 22 18"><rect x="1" y="3" width="20" height="14" rx="2" fill="#999"/><rect x="4" y="0" width="13" height="4" fill="#bbb"/><rect x="14" y="8" width="7" height="5" fill="#eee"/></svg></div>
  <div><h4>EASY PAYMENT</h4><p>Lorem Ipsum is simply</p></div>
</div>
<div class="abs feature" style="left:823px">
  <div class="ring"><svg width="22" height="22" viewBox="0 0 22 22"><circle cx="11" cy="11" r="9.5" fill="none" stroke="#999" stroke-width="2"/><path d="M6 11l4 4 6-7" fill="none" stroke="#999" stroke-width="2.4"/></svg></div>
  <div><h4>100% GENUINE</h4><p>Lorem Ipsum is simply</p></div>
</div>

<!-- products -->
<div class="abs section-rule" style="top:792px"></div>
<h2 class="abs section-title" style="top:794px">Our Product</h2>
<div class="abs section-rule" style="top:846px"></div>

<div class="abs product" style="left:199px;top:889px">
  <div class="thumb" style="position:relative;background:radial-gradient(ellipse at 50% 48%,#8fc4a0 0%,#a9d3b4 28%,#f5f5f5 50%)" role="img" aria-label="Green stone elephant figurine">
    <div class="abs quick-tools">
      <span><svg width="11" height="10" viewBox="0 0 24 22"><path d="M12 21L2 11a6 6 0 0 1 10-7 6 6 0 0 1 10 7z" fill="#fff"/></svg></span>
      <span><svg width="10" height="10" viewBox="0 0 20 20"><path d="M2 2l16 16M18 2L2 18" stroke="#fff" stroke-width="3"/></svg></span>
      <span><svg width="12" height="11" viewBox="0 0 26 22"><path d="M1 2h4l3 12h13l3-9H7" fill="none" stroke="#fff" stroke-width="2.6"/><circle cx="10" cy="19" r="2" fill="#fff"/><circle cx="19" cy="19" r="2" fill="#fff"/></svg></span>
    </div>
  </div>
  <h3>OPALITE</h3><div class="price">$950.00</div><div class="add">Add To Cart</div>
</div>
<div class="abs product" style="left:406px;top:889px">
  <div class="thumb" style="background:radial-gradient(ellipse at 50% 50%,#e6606a 0%,#ee8a90 25%,#f5f5f5 48%)" role="img" aria-label="Pair of pink red stone elephant figurines"></div>
  <h3>GREEN AVENTURINE</h3><div class="price">$950.00</div><div class="add">Add To Cart</div>
</div>
<div class="abs product" style="left:610px;top:889px">
  <div class="thumb" style="background:radial-gradient(ellipse at 50% 50%,#8a5a22 0%,#b07a36 22%,#f5f5f5 45%)" role="img" aria-label="Tiger eye stone angel figurine"></div>
  <h3>WATERMELON CRYSTAL</h3><div class="price">$950.00</div><div class="add">Add To Cart</div>
</div>
<div class="abs product" style="left:815px;top:889px">
  <div class="thumb" style="background:radial-gradient(ellipse at 50% 50%,#3a2a1e 0%,#5e4430 24%,#f5f5f5 48%)" role="img" aria-label="Pair of dark tiger eye stone elephant figurines"></div>
  <h3>TIGER EYE STONE</h3><div class="price">$950.00</div><div class="add">Add To Cart</div>
</div>

<div class="abs product" style="left:199px;top:1210px">
  <div class="thumb" style="background:radial-gradient(ellipse at 50% 50%,#1f6b3e 0%,#3d8a58 24%,#f5f5f5 48%)" role="img" aria-label="Pair of green aventurine elephant figurines"></div>
  <h3>OPALITE</h3><div class="price">$950.00</div><div class="add">Add To Cart</div>
</div>
<div class="abs product" style="left:406px;top:1210px">
  <div class="thumb" style="background:radial-gradient(ellipse at 50% 50%,#4a4430 0%,#6a6244 20%,#f5f5f5 42%)" role="img" aria-label="Dark pyrite stone angel figurine"></div>
  <h3>GREEN AVENTURINE</h3><div class="price">$950.00</div><div class="add">Add To Cart</div>
</div>
<div class="abs product" style="left:610px;top:1210px">
  <div class="thumb" style="background:radial-gradient(ellipse at 50% 50%,#b9d6ee 0%,#d7e7f4 28%,#f5f5f5 50%)" role="img" aria-label="Milky blue opalite elephant figurine"></div>
  <h3>WATERMELON CRYSTAL</h3><div class="price">$950.00</div><div class="add">Add To Cart</div>
</div>
<div class="abs product" style="left:815px;top:1210px">
  <div class="thumb" style="background:radial-gradient(ellipse at 50% 50%,#e2a3c6 0%,#ecbfd6 26%,#f5f5f5 48%)" role="img" aria-label="Pair of rose quartz elephant figurines"></div>
  <h3>TIGER EYE STONE</h3><div class="price">$950.00</div><div class="add">Add To Cart</div>
</div>

<!-- blog -->
<div class="abs section-rule" style="top:1550px"></div>
<h2 class="abs section-title" style="top:1552px">Latest Blog</h2>
<div class="abs section-rule" style="top:1604px"></div>

<svg class="abs blog-arrows" width="24" height="10" viewBox="0 0 24 10"><path d="M1 5h9M1 5l3-3M1 5l3 3M14 5h9M23 5l-3-3M23 5l-3 3" stroke="#111" stroke-width="1.4" fill="none"/></svg>

<article class="abs post" style="left:199px">
  <div class="day">03</div>
  <div class="month">/ MARCH<br>2018</div>
  <div class="headline">LOREM IPSUM IS SIMP DUMMY TEXT HERE..</div>
  <div class="meta">03/03/2018 <i></i>
    <svg width="13" height="12" viewBox="0 0 26 24"><path d="M2 2h22v14H10l-6 6v-6H2z" fill="none" stroke="#c08a2e" stroke-width="2.4"/></svg>2 Comments</div>
  <div class="photo" style="background:radial-gradient(circle at 50% 50%,#2c2c2c 0%,#2c2c2c 28%,#c8b9b0 45%,#9aa6b0 62%,#303030 80%)" role="img" aria-label="Ring of assorted crystal angel figurines on a dark background"></div>
</article>

<article class="abs post" style="left:613px">
  <div class="day">03</div>
  <div class="month">/ MARCH<br>2018</div>
  <div class="headline">LOREM IPSUM IS SIMP DUMMY TEXT HERE..</div>
  <div class="meta">03/03/2018 <i></i>
    <svg width="13" height="12" viewBox="0 0 26 24"><path d="M2 2h22v14H10l-6 6v-6H2z" fill="none" stroke="#c08a2e" stroke-width="2.4"/></svg>2 Comments</div>
  <div class="photo" style="background:radial-gradient(ellipse at 50% 45%,#b04a3a 0%,#9a7a98 25%,#5a4a3a 45%,#0c0c10 70%)" role="img" aria-label="Assorted polished tumbled healing stones on a black background"></div>
</article>

<!-- newsletter & footer -->
<section class="abs newsletter" role="img" aria-label="Soft faded background of smooth pebbles">
  <svg style="position:absolute;left:582px;top:64px" width="36" height="34" viewBox="0 0 36 34"><path d="M2 14L18 2l16 12v18H2z" fill="#111"/><rect x="9" y="7" width="18" height="13" fill="#fff"/><path d="M12 11h12M12 15h9" stroke="#111" stroke-width="2"/><path d="M2 14l16 11 16-11" fill="none" stroke="#fff" stroke-width="2"/></svg>
  <h2>JOIN OUR NEWSLETTER !</h2>
  <p class="lead">Lorem Ipsum is simply dummy text of the printing industry</p>
  <div class="email-field">Enter Your Email</div>
  <div class="signup-btn">SIGN UP</div>
  <div class="social-row">
    <span class="label">OR SIGN UP ON</span>
    <span class="social-btn chirper"><i></i>Chirper</span>
    <span class="social-btn searchly"><i></i>Searchly</span>
    <span class="social-btn friendbook"><i></i>Friendbook</span>
  </div>
  <div class="footer-rule" style="top:292px"></div>
  <div class="footer-links"><span>Home</span><span>/</span><span>About Us</span><span>/</span><span>Product</span><span>/</span><span>Blog</span><span>/</span><span>Contact Us</span></div>
  <div class="footer-rule" style="top:327px"></div>
  <div class="copyright">© Copyright 2018 Lumara Bloom House. All Rights Reserved.</div>
</section>

</body>
</html>
```